Business Card and Stationary Design

After the successful redesign of our logo we are wanting to follow suite and create a new business card and stationary design!

New Logo is attached, information required on the business card should contain a mixture of the following but layout/arrangement is up to the designer.

Happy if the national provider number and abn are on the back, and happy for them to be smaller than the rest.

I am also happy to receive single sided or weird and wonderful designs.

Name
Title
National Provider Number 7192
ABN 53 614 289 117
Level 1, 214 Garrow Street
Brenmore NSW 2291
Ph: 1300 587 902
Mobile: 0438 761 205
name@ironquillbuild.com.au
www.ironquillbuild.com.au

Target Market(s)

Professionals, Peers, Students, Suppliers...

Industry/Entity Type

Construction

Contact Information for Business Card

Listed in project description

Font styles to use
Other font styles liked:
• Century Gothic

Colors
0455a3
3176b5
ffffff

Requirements
Must have
• Professional Design, same color scheme as our logo
Nice to have
• Something that sets our apart from everyone else would be fantastic, open to size and shape and layout options, as long as they present professionally.
• Open to raised/embossed text, alternative materials, custom sizes, clear material
Should not have
• The color orange

```html
<!DOCTYPE html>
<html lang="en">
<head>
<meta charset="utf-8">
<title>Ironquill Build – Business Card</title>
<link href="https://fonts.googleapis.com/css2?family=Open+Sans:wght@400;700&display=swap" rel="stylesheet">
<style>
  :root {
    --backdrop: #2b2b2b;
    --card-grey: #7f7f7f;
    --card-blue: #1f3a78;
    --card-white: #f1f1f1;
    --brand-blue: #1f3a78;
    --text-light: #ffffff;
    --divider: #ffffff;
  }
  * { margin: 0; padding: 0; box-sizing: border-box; }
  html, body {
    width: 1200px; height: 960px; overflow: hidden;
    background: var(--backdrop);
    font-family: "Open Sans", Arial, sans-serif;
  }
  .canvas { position: relative; width: 1200px; height: 960px; }

  .card { position: absolute; width: 600px; height: 343px; overflow: hidden; }
  .card--front { left: 314px; top: 113px; background: var(--card-white); }
  .card--back { left: 311px; top: 472px; background: var(--card-grey); }

  .identity {
    position: absolute; left: 0; top: 0; width: 273px; height: 108px;
    background: var(--card-grey); color: var(--text-light);
    padding: 29px 0 0 28px;
  }
  .identity__name { font-weight: 700; font-size: 19px; line-height: 25px; letter-spacing: -0.3px; }
  .identity__title { font-size: 15px; line-height: 20px; }

  .divider { position: absolute; left: 0; top: 108px; width: 273px; height: 3px; background: var(--divider); }

  .details {
    position: absolute; left: 0; top: 111px; width: 273px; height: 232px;
    background: var(--card-blue); color: var(--text-light);
    padding: 31px 0 0 28px; font-size: 14.5px; line-height: 20.5px;
  }
  .details__block { margin-bottom: 1px; }
  .details__block + .details__block { margin-bottom: 6px; }
  .contact { list-style: none; line-height: 19.2px; }
  .contact li { display: flex; align-items: center; }
  .contact svg { width: 14px; height: 14px; margin-right: 8px; fill: var(--text-light); flex: none; }

  .brand { position: absolute; display: flex; align-items: center; color: var(--brand-blue); font-weight: 400; }
  .brand__mark { background: var(--brand-blue); flex: none; }
  .card--front .brand { left: 316px; top: 152px; font-size: 27px; }
  .card--front .brand__mark { width: 34px; height: 34px; margin-right: 10px; }
  .card--back .brand { left: 0; width: 600px; justify-content: center; top: 130px; font-size: 44px; color: var(--text-light); }
  .card--back .brand__mark { width: 54px; height: 54px; margin-right: 16px; background: var(--text-light); }

  .web {
    position: absolute; left: 0; width: 600px; top: 286px; text-align: center;
    color: var(--text-light); font-size: 15px; letter-spacing: 7px;
  }
</style>
</head>
<body>
<main class="canvas">
  <section class="card card--front" aria-label="Business card front">
    <div class="identity">
      <p class="identity__name">DANIEL HARTLEY</p>
      <p class="identity__title">CEO/FOUNDER</p>
    </div>
    <div class="divider"></div>
    <div class="details">
      <p class="details__block">Level 1, 214 Garrow Street<br>Brenmore NSW 2291</p>
      <p class="details__block">National Provider Number 7192<br>ABN 53 614 289 117</p>
      <ul class="contact">
        <li><svg viewBox="0 0 16 16" aria-hidden="true"><path d="M1 5c0-2 3-3 7-3s7 1 7 3v1h-4V5H5v1H1zM4 7h8l2 7H2z"/></svg>1300 587 902</li>
        <li><svg viewBox="0 0 16 16" aria-hidden="true"><path d="M4 1h8v14H4zM5.5 3v9h5V3z"/></svg>0438 761 205</li>
        <li><svg viewBox="0 0 16 16" aria-hidden="true"><path d="M2 4h12v1L8 9 2 5zM2 6.5l6 4 6-4V12H2z"/></svg>name@ironquillbuild.com.au</li>
        <li><svg viewBox="0 0 16 16" aria-hidden="true"><circle cx="8" cy="8" r="6.5"/></svg>www.ironquillbuild.com.au</li>
      </ul>
    </div>
    <div class="brand"><span class="brand__mark"></span><span class="brand__name">ironquill build</span></div>
  </section>

  <section class="card card--back" aria-label="Business card back">
    <div class="brand"><span class="brand__mark"></span><span class="brand__name">ironquill build</span></div>
    <p class="web">www.ironquillbuild.com.au</p>
  </section>
</main>
</body>
</html>
```